VALMIRA/ VALMIRA GREY Business Card

We have two brands that we would like to show one 1 business card (front and back). We would to incorporate two different logos on one card (VALMIRA and VALMIRA GREY). Card can be two sided. Simple, sleek and professional.

We are a senior living provider.

www.valmira-example.com
www.valmiragrey-example.com

Target Market(s)

Professionals

Industry/Entity Type

Business

Font styles to use
Serif

Colors

Designer to choose colors to be used in the design.

Requirements
Must have
• Space for EMAIL, PHONE, WEBSITE
Nice to have
• Raised lettering or gloss lettering

```html
<!DOCTYPE html>
<html lang="en">
<head>
<meta charset="utf-8">
<title>Valmira / Valmira Grey Business Card</title>
<link href="https://fonts.googleapis.com/css2?family=Cinzel:wght@400;500&family=Montserrat:wght@300;400&display=swap" rel="stylesheet">
<style>
  :root {
    --page: #ececec;
    --card-dark: #050505;
    --card-mid: #1c1c1c;
    --gold: #c9a13c;
    --gold-light: #d9b653;
    --gold-deep: #a9822a;
    --white: #f2f2f2;
    --muted: #cfcfcf;
  }
  * { margin: 0; padding: 0; box-sizing: border-box; }
  html, body {
    width: 1003px; height: 1200px; overflow: hidden;
    background: var(--page);
    font-family: "Montserrat", sans-serif;
  }
  .card {
    position: absolute; left: 117px; width: 770px; height: 466px;
    border: 14px solid var(--gold);
    border-image: linear-gradient(135deg, var(--gold-light), var(--gold-deep), var(--gold-light)) 1;
    background: radial-gradient(ellipse at 50% 50%, var(--card-mid) 0%, var(--card-dark) 75%);
  }
  .card-front { top: 85px; }
  .card-back { top: 652px; }

  .brand {
    position: absolute; display: flex; align-items: center; gap: 12px;
    font-family: "Cinzel", serif; color: var(--gold); letter-spacing: 2px;
  }
  .brand-mark { width: 14px; height: 14px; background: var(--gold); }
  .brand-primary { font-size: 46px; font-weight: 400; }
  .brand-secondary { font-size: 30px; color: var(--white); }
  .brand-secondary .brand-mark { background: var(--white); width: 12px; height: 12px; }
  .tagline {
    position: absolute; font-size: 14px; color: var(--muted); letter-spacing: 0.3px;
  }

  /* front */
  .front-brand-primary { left: 62px; top: 82px; }
  .front-brand-secondary { left: 62px; top: 168px; }
  .front-tagline { left: 88px; top: 212px; }
  .divider {
    position: absolute; left: 375px; top: 60px; width: 1px; height: 330px;
    background: linear-gradient(to bottom, transparent, #bdbdbd 50%, transparent);
  }
  .person {
    position: absolute; left: 395px; top: 12px;
  }
  .person-name { font-size: 25px; font-weight: 300; color: var(--gold); letter-spacing: 3px; }
  .person-role { font-size: 17px; color: var(--white); letter-spacing: 4px; margin-top: 6px; }
  .person-address { font-size: 17px; color: var(--white); line-height: 26px; margin-top: 12px; }
  .contact-list { list-style: none; margin-top: 28px; }
  .contact-list li {
    display: flex; align-items: center; gap: 14px;
    font-size: 17px; color: var(--white); height: 28px;
  }
  .contact-icon { width: 14px; height: 14px; flex: none; }
  .contact-dot { width: 10px; height: 10px; margin: 0 2px; background: var(--gold); flex: none; }

  /* back */
  .back-center { position: absolute; left: 0; right: 0; text-align: center; }
  .back-brand-primary { position: absolute; left: 50%; top: 40px; transform: translateX(-50%); }
  .back-url { font-size: 17px; color: var(--white); letter-spacing: 4px; text-transform: uppercase; }
  .back-url-primary { top: 118px; }
  .back-brand-secondary { position: absolute; left: 50%; top: 184px; transform: translateX(-50%); }
  .back-tagline { top: 228px; font-size: 14px; color: var(--muted); }
  .back-url-secondary { top: 274px; }
</style>
</head>
<body>

<section class="card card-front">
  <div class="brand brand-primary front-brand-primary"><span class="brand-mark"></span>VALMIRA</div>
  <div class="brand brand-secondary front-brand-secondary"><span class="brand-mark"></span>VALMIRA GREY</div>
  <div class="tagline front-tagline">Executive Personal Care Services</div>

  <div class="divider"></div>

  <div class="person">
    <div class="person-name">CLARA WHITFIELD</div>
    <div class="person-role">CEO</div>
    <div class="person-address">Larkspur Bend, Idaho and<br>Hollow Ridge, NY</div>
    <ul class="contact-list">
      <li>
        <svg class="contact-icon" viewBox="0 0 24 24"><path fill="#c9a13c" d="M6.6 10.8a15 15 0 0 0 6.6 6.6l2.2-2.2c.3-.3.7-.4 1-.2 1.1.4 2.3.6 3.6.6.6 0 1 .4 1 1V20c0 .6-.4 1-1 1A17 17 0 0 1 3 4c0-.6.4-1 1-1h3.5c.6 0 1 .4 1 1 0 1.3.2 2.5.6 3.6.1.3 0 .7-.2 1z"/></svg>
        0555 0147 22
      </li>
      <li>
        <svg class="contact-icon" viewBox="0 0 24 24"><rect x="2" y="5" width="20" height="14" fill="#c9a13c"/><path d="M2 5l10 8 10-8" fill="none" stroke="#050505" stroke-width="2"/></svg>
        clara@valmira-example.com
      </li>
      <li><span class="contact-dot"></span>@clarawhitfield</li>
      <li><span class="contact-dot"></span>@claravalmira</li>
      <li><span class="contact-dot"></span>@claravalmira</li>
      <li><span class="contact-dot"></span>@claravalmira</li>
    </ul>
  </div>
</section>

<section class="card card-back">
  <div class="brand brand-primary back-brand-primary"><span class="brand-mark"></span>VALMIRA</div>
  <div class="back-center back-url back-url-primary">www.valmira-example.com</div>
  <div class="brand brand-secondary back-brand-secondary"><span class="brand-mark"></span>VALMIRA GREY</div>
  <div class="back-center back-tagline">Executive Personal Care Services</div>
  <div class="back-center back-url back-url-secondary">www.valmiragrey-example.com</div>
</section>

</body>
</html>
```